Business Card Design for Photographer

Updating business card design. Must use included logo. We're a luxury wedding photography business. Elegancy, luxury, consistency are messages we wish to convey.

Visit our website at www.colbyvarnway.com to familiarize yourself more with our brand design currently (fonts, colors etc.). This is what we want to maintain.

Target Market(s)

Luxury Brides and Grooms

Industry/Entity Type

Wedding

Contact Information for Business Card

Current logo (attached to brief)
Name: Colby Varnway
Phone: 5208813047
website/blog
Email

Requirements
Must have
• Current logo (attached to brief)
• Name: Colby Varnway
• Phone: 5208813047
• website/blog
• Email
• Instagram username
Should not have
• bright colors, fonts that don't suit our brand (visit www.colbyvarnway.com)

```html
<!DOCTYPE html>
<html lang="en">
<head>
<meta charset="utf-8">
<title>Colby Varnway Photographers – Business Card</title>
<link rel="stylesheet" href="https://fonts.googleapis.com/css2?family=EB+Garamond:wght@400;600&family=Marcellus&display=swap">
<style>
  :root {
    --backdrop: #2a2a2a;
    --card-front-light: #ffffff;
    --card-front-mid: #f0f0f0;
    --card-front-edge: #dcdcdc;
    --card-back: #6b6b6b;
    --card-back-dark: #646464;
    --ink: #5a5a5a;
    --ink-soft: #6e6e6e;
    --on-dark: #ffffff;
  }
  * { margin: 0; padding: 0; box-sizing: border-box; }
  html, body { width: 1200px; height: 848px; overflow: hidden; }
  body { background: var(--backdrop); position: relative; font-family: "EB Garamond", Georgia, serif; }

  .card {
    position: absolute;
    left: 318px;
    width: 510px;
    height: 306px;
    box-shadow: 0 10px 24px rgba(0,0,0,0.55);
  }
  .card--front {
    top: 96px;
    background: radial-gradient(ellipse at 72% 30%, var(--card-front-light) 0%, var(--card-front-mid) 45%, var(--card-front-edge) 100%);
    color: var(--ink);
  }
  .card--back {
    top: 426px;
    background: linear-gradient(135deg, var(--card-back) 0%, var(--card-back-dark) 100%);
    color: var(--on-dark);
  }

  .brand {
    position: absolute;
    text-align: center;
    font-family: "Marcellus", "Times New Roman", serif;
  }
  .brand__mark {
    display: block;
    margin: 0 auto 10px;
    width: 26px;
    height: 26px;
    background: currentColor;
  }
  .brand__name {
    display: block;
    font-size: 21px;
    letter-spacing: 4px;
    text-transform: uppercase;
    white-space: nowrap;
  }
  .brand__tagline {
    display: block;
    margin-top: 6px;
    font-size: 10px;
    letter-spacing: 4.5px;
    text-transform: uppercase;
  }
  .card--front .brand { right: 36px; top: 46px; width: 250px; }
  .card--back .brand { left: 180px; top: 180px; width: 260px; }
  .card--back .brand__mark { width: 40px; height: 40px; margin-bottom: 16px; }

  .contact {
    position: absolute;
    right: 16px;
    top: 176px;
    text-align: right;
  }
  .contact__name {
    font-weight: 600;
    font-size: 15px;
    letter-spacing: 0.5px;
    text-transform: uppercase;
    margin-right: 14px;
    margin-bottom: 9px;
    color: var(--ink);
  }
  .contact__list { list-style: none; }
  .contact__item {
    display: flex;
    justify-content: flex-end;
    align-items: center;
    gap: 6px;
    font-size: 13.5px;
    line-height: 18px;
    color: var(--ink-soft);
  }
  .contact__icon { width: 10px; height: 10px; flex: none; }
</style>
</head>
<body>

<section class="card card--front" aria-label="Card front">
  <div class="brand">
    <span class="brand__mark" aria-hidden="true"></span>
    <span class="brand__name">Colby Varnway</span>
    <span class="brand__tagline">Photographers</span>
  </div>

  <div class="contact">
    <p class="contact__name">Colby Varnway</p>
    <ul class="contact__list">
      <li class="contact__item">(520) 881-3047
        <svg class="contact__icon" viewBox="0 0 10 10" aria-hidden="true"><path d="M1 4 Q1 1 5 1 Q9 1 9 4 L7 4 L7 3 L3 3 L3 4 Z M2 5 L8 5 L9 9 L1 9 Z" fill="#666"/></svg>
      </li>
      <li class="contact__item">colby@colbyvarnway.com
        <svg class="contact__icon" viewBox="0 0 10 10" aria-hidden="true"><rect x="0.5" y="2" width="9" height="6.5" fill="#666"/><path d="M0.5 2 L5 5.5 L9.5 2" stroke="#ddd" stroke-width="0.8" fill="none"/></svg>
      </li>
      <li class="contact__item">colbyvarnway.com
        <svg class="contact__icon" viewBox="0 0 10 10" aria-hidden="true"><circle cx="5" cy="5" r="4.5" fill="#666"/><path d="M0.5 5 H9.5 M5 0.5 V9.5 M5 0.5 Q2 5 5 9.5 M5 0.5 Q8 5 5 9.5" stroke="#ddd" stroke-width="0.6" fill="none"/></svg>
      </li>
      <li class="contact__item">colbyvarnwayphoto
        <svg class="contact__icon" viewBox="0 0 10 10" aria-hidden="true"><rect x="0.5" y="0.5" width="9" height="9" fill="#666"/></svg>
      </li>
    </ul>
  </div>
</section>

<section class="card card--back" aria-label="Card back">
  <div class="brand">
    <span class="brand__mark" aria-hidden="true"></span>
    <span class="brand__name">Colby Varnway</span>
    <span class="brand__tagline">Photographers</span>
  </div>
</section>

</body>
</html>
```